PLEASE READ - DESIGN for Music Cover Tunora - DJ and Female Singer

A nice cover to be put on Tunora.
Definitely will be on Tunora and All Media
Name of the song: Lumenvaria
Singer name: Maris Oldenquay
DJ name: DJ Rolf Tamsek

Lumenvaria definition: A desire to be in the Sun

We need eye catching icon or something that can attract people's eyes when they see it immediately. Design must be elegant. This is not some type of Club Banging Music. The singer is a romantic and sophisticated audiophile jazz acoustic recording artist. DJ is not playing in some clubs but exclusive.

Photo of singer and DJ can be on the cover OR just photo of the singer OR just an Icon wifh their names and the song name.

Avoid these colors: Pink, Purple, Silver !!
For the background color try: A mixed of Black or Gold with Elegant Yellow, Pastel Orange, or light Blue.
For name of the song and Icon color : can be of Gold or even Red or White.
Or you can try and mix it all up yourself

Icon ideas: can be a combination of letter Capital C with small B & Capital V alone or mixed with a sun logo or half of Sun. Some cool stuff.
MO is Maris Oldenquay
V is for the DJ name

Target Market(s)

Young Adult, Lounge Crowd, Club Goers / Lounge Goers, Ladies, Executives, Adults, Music Industry

Industry/Entity Type

Entertainment Industry

Font styles to use
Serif

Requirements
Must have
• LUMENVARIA ( song name )
• Available on Tunora logo
• EYE CATCHING ICON or LOGO
Should not have
• Avoid this color :
• Pink, Purple, Silver, White
• Our first project was already consisting these colors, we will attach the old design of the first song but PLEASE DO NOT apply the older design to this new project :)

```html
<!DOCTYPE html>
<html lang="en">
<head>
<meta charset="utf-8">
<title>Lumenvaria — Rolf Tamsek feat Maris Oldenquay</title>
<link rel="stylesheet" href="https://fonts.googleapis.com/css2?family=Cinzel+Decorative:wght@700&family=Poiret+One&display=swap">
<style>
  :root {
    --bg: #000000;
    --gold-light: #fff2a6;
    --gold: #e3b321;
    --gold-deep: #8a5f08;
    --credit: #d8d19c;
    --badge-text: #ffffff;
    --badge-line: #a6a6a6;
  }
  html, body {
    margin: 0;
    padding: 0;
    width: 1200px;
    height: 1200px;
    overflow: hidden;
    background: var(--bg);
  }
  .cover {
    position: relative;
    width: 1200px;
    height: 1200px;
    background: var(--bg);
    overflow: hidden;
  }
  .song-title {
    position: absolute;
    top: 128px;
    left: 0;
    width: 100%;
    margin: 0;
    text-align: center;
    font-family: "Cinzel Decorative", "Times New Roman", serif;
    font-weight: 700;
    font-size: 104px;
    letter-spacing: 2px;
    line-height: 1;
    background: linear-gradient(180deg, var(--gold-light) 0%, var(--gold) 45%, var(--gold-deep) 60%, var(--gold) 80%, var(--gold-light) 100%);
    -webkit-background-clip: text;
    background-clip: text;
    color: transparent;
  }
  .sun-emblem {
    position: absolute;
    left: 300px;
    top: 250px;
    width: 600px;
    height: 600px;
  }
  .credits {
    position: absolute;
    top: 812px;
    left: 0;
    width: 100%;
    text-align: center;
    font-family: "Poiret One", "Helvetica", sans-serif;
    color: var(--credit);
    letter-spacing: 3px;
  }
  .credits p { margin: 0; }
  .credits .artist { font-size: 46px; line-height: 62px; }
  .credits .feat { font-size: 40px; line-height: 62px; }
  .store-badge {
    position: absolute;
    left: 514px;
    top: 1062px;
    width: 172px;
    height: 64px;
    box-sizing: border-box;
    border: 2px solid var(--badge-line);
    border-radius: 10px;
    background: var(--bg);
    display: flex;
    flex-direction: column;
    justify-content: center;
    align-items: center;
    font-family: "Poiret One", "Helvetica", sans-serif;
    color: var(--badge-text);
    line-height: 1.1;
  }
  .store-badge .small { font-size: 15px; }
  .store-badge .name { font-size: 26px; }
</style>
</head>
<body>
  <main class="cover">
    <h1 class="song-title">Lumenvaria</h1>

    <svg class="sun-emblem" viewBox="0 0 600 600" role="img" aria-label="Golden sunburst emblem with an eye-like dark centre">
      <defs>
        <radialGradient id="sunGlow" cx="50%" cy="50%" r="50%">
          <stop offset="0%" stop-color="#000000"/>
          <stop offset="20%" stop-color="#000000"/>
          <stop offset="28%" stop-color="#f3c625"/>
          <stop offset="55%" stop-color="#c99a14" stop-opacity="0.7"/>
          <stop offset="80%" stop-color="#4a3c0c" stop-opacity="0.35"/>
          <stop offset="100%" stop-color="#000000" stop-opacity="0"/>
        </radialGradient>
      </defs>
      <circle cx="300" cy="300" r="300" fill="url(#sunGlow)"/>
    </svg>

    <div class="credits">
      <p class="artist">ROLF TAMSEK</p>
      <p class="feat">FEAT</p>
      <p class="artist">MARIS OLDENQUAY</p>
    </div>

    <div class="store-badge">
      <span class="small">Available on</span>
      <span class="name">Tunora</span>
    </div>
  </main>
</body>
</html>
```